ALL TEXT Social Media Graphics

We are looking for a series of social media graphics for Instagram (new size: 4:5 (1080 x 1350 pixels) ratio that are ALL TEXT. We want the following quotes below on each graphic; one quote per graphic. AND, In very small letters at the bottom of each graphic, add @PaulaWrenLive
The look and feel of these graphics should be complimentary to the color palette attached below; but keep them simple. But the design is up to you; at the end of this document, I provided various samples of all text graphics that I like as examples.
The Quotes are in the attached WORD document
women trying to lose weight

```html
<!DOCTYPE html>
<html lang="en">
<head>
<meta charset="utf-8">
<title>Glow Up Summer Reset</title>
<link href="https://fonts.googleapis.com/css2?family=Montserrat:wght@800&family=Roboto:wght@500&family=Inter:wght@500&display=swap" rel="stylesheet">
<style>
  :root {
    --pink: #ee3f8e;
    --slate: #2f5260;
    --berry: #a11c58;
    --handle: #33444d;
    --bg-top: #ffffff;
    --bg-bottom: #fbc3d5;
  }
  html, body {
    margin: 0;
    padding: 0;
    width: 960px;
    height: 1200px;
    overflow: hidden;
  }
  .post {
    position: relative;
    width: 960px;
    height: 1200px;
    background: linear-gradient(to bottom, var(--bg-top) 0%, var(--bg-top) 61%, #fde3ec 80%, var(--bg-bottom) 100%);
  }
  .headline {
    position: absolute;
    top: 100px;
    left: 70px;
    margin: 0;
    font-family: "Montserrat", sans-serif;
    font-weight: 800;
    font-size: 68px;
    line-height: 97px;
    letter-spacing: -0.8px;
    color: var(--pink);
  }
  .promise {
    position: absolute;
    top: 452px;
    left: 70px;
    margin: 0;
    font-family: "Montserrat", sans-serif;
    font-weight: 800;
    font-size: 60px;
    line-height: 85px;
    letter-spacing: -0.8px;
    color: var(--slate);
  }
  .call-to-action {
    position: absolute;
    top: 688px;
    left: 70px;
    margin: 0;
    font-family: "Roboto", sans-serif;
    font-weight: 500;
    font-size: 68px;
    line-height: 83px;
    letter-spacing: 1px;
    color: var(--berry);
  }
  .handle {
    position: absolute;
    top: 1036px;
    left: 70px;
    margin: 0;
    font-family: "Inter", sans-serif;
    font-weight: 500;
    font-size: 40px;
    color: var(--handle);
  }
</style>
</head>
<body>
  <main class="post">
    <h1 class="headline">You can absolutely be<br>down 20–30 pounds<br>by end of summer.</h1>
    <p class="promise">All it takes is the right<br>plan—and you’ve found it.</p>
    <p class="call-to-action">Comment GLOW UP<br>for the Glow Up<br>Summer Reset!</p>
    <p class="handle">@PaulaWrenLive</p>
  </main>
</body>
</html>
```